KMR Business cards

I currently have a logo that was designed by a pixel harbor designer. I would like this to be added to the business card.

We are an innovative new start-up business offering finance solutions to the car dealership market in the UK. So our clients are quiet traditional, so are cards need to fit in, but at the same time show we are a modern online business.

Finance

```html
<!DOCTYPE html>
<html lang="en">
<head>
<meta charset="utf-8">
<title>KMR Business Cards</title>
<link rel="stylesheet" href="https://fonts.googleapis.com/css2?family=Arimo:wght@400;500&display=swap">
<style>
  :root {
    --navy: #132a4e;
    --paper: #ffffff;
    --backdrop: #ffffff;
    --shadow: rgba(0, 0, 0, 0.6);
  }
  html, body {
    margin: 0;
    padding: 0;
    overflow: hidden;
    background: var(--backdrop);
  }
  .canvas {
    position: relative;
    width: 1200px;
    height: 1000px;
    overflow: hidden;
    background: var(--backdrop);
    font-family: "Arimo", Arial, sans-serif;
    color: var(--navy);
  }
  .card {
    position: absolute;
    top: 213px;
    width: 298px;
    height: 522px;
    box-shadow: 6px 6px 7px var(--shadow);
  }
  .card--front {
    left: 247px;
    background: var(--navy);
  }
  .card--back {
    left: 661px;
    background: var(--paper);
  }
  .front-brand {
    position: absolute;
    left: 0;
    right: 0;
    top: 232px;
    display: flex;
    align-items: center;
    justify-content: center;
    gap: 14px;
  }
  .front-brand-dot {
    width: 34px;
    height: 34px;
    border-radius: 50%;
    background: var(--paper);
  }
  .front-brand-name {
    color: var(--paper);
    font-size: 52px;
    line-height: 56px;
    font-weight: 500;
  }
  .band {
    position: absolute;
    left: 103px;
    right: 0;
    height: 9px;
    background: var(--navy);
  }
  .band--top { top: 42px; }
  .band--bottom { top: 139px; }
  .brand {
    position: absolute;
    left: 149px;
    top: 62px;
    display: flex;
    align-items: center;
    gap: 8px;
  }
  .brand-dot {
    width: 58px;
    height: 58px;
    border: 3px solid var(--navy);
    border-radius: 50%;
    box-sizing: border-box;
  }
  .brand-name {
    font-size: 18px;
    font-weight: 400;
    line-height: 20px;
    color: var(--navy);
  }
  .contact {
    position: absolute;
    left: 16px;
    font-size: 14px;
    line-height: 17px;
    font-weight: 400;
  }
  .contact p { margin: 0; }
  .contact--person { top: 353px; }
  .contact--lines { top: 403px; left: 19px; }
  .contact--email { top: 487px; }
</style>
</head>
<body>
<div class="canvas">
  <section class="card card--front" aria-label="Card front">
    <div class="front-brand">
      <div class="front-brand-dot"></div>
      <div class="front-brand-name">KMR</div>
    </div>
  </section>

  <section class="card card--back" aria-label="Card back">
    <div class="band band--top"></div>
    <div class="brand">
      <div class="brand-dot"></div>
      <div class="brand-name">Kestrel<br>Motor<br>Reserve</div>
    </div>
    <div class="band band--bottom"></div>

    <div class="contact contact--person">
      <p>OLIVER PRESTON</p>
      <p>Founder</p>
    </div>
    <div class="contact contact--lines">
      <p>07700 900418</p>
      <p>oliver.preston_kmr</p>
      <p>www.kestrelmotorreserve.com</p>
    </div>
    <div class="contact contact--email">
      <p>oliver.preston@kestrelmotorreserve.com</p>
    </div>
  </section>
</div>
</body>
</html>
```